vireLattice "organisation chart"

We need a new Organisation Chart for our Company! We are actually in a Change-management-process and will Change from a hierarchical Organisation in to a Network Organisation. Therefor we need a new Organisation Chart.
The following departements must be visible and legible on the Chart:
Team Sales & Consulting
Team Productmanagement
Team Supply Chain
Team Human Resources
Team Smart Digital Development
Team Marketing & Communication
The title of the Chart ist «vireLattice»
The Colors of the back of the Chart must be: RGB 73/25/102 // Pantone 2627
The Colors for the different Teams should be:
Team Sales & Consulting (Pantone: 803/neon yellow = Background)
Team Productmanagement (Pantone: 804/neon orange = Background)
Team Supply Chain (Pantone: 802/neon green = Background)
Team Human Resources (Pantone: 801/neon blue = Background)
Team Smart Digital Development (Pantone: 805/neon red = Background)
Team Marketing & Communication (Pantone: 803/neon pink = Background)
See below (upload files) an example showing a self-made Chart ... :-)
Our font is: Univers LT Std // Please feel free to Combine the Fonts Colors with the background colors
It Company

```html
<!DOCTYPE html>
<html lang="en">
<head>
<meta charset="utf-8">
<title>vireLattice – Organisation Chart</title>
<link rel="stylesheet" href="https://fonts.googleapis.com/css2?family=Arimo:wght@400;700&display=swap">
<style>
  :root {
    --bg: #6c3a8b;
    --line: #ffffff;
    --title: #ffffff;
    --yellow: #f6e31c;
    --yellow-shade: #d9c300;
    --yellow-ink: #f0961e;
    --orange: #ffa548;
    --orange-shade: #e5852a;
    --orange-ink: #e8461d;
    --green: #2fd043;
    --green-shade: #16a82c;
    --green-ink: #0b5e1e;
    --green-ring: #b8f5a4;
    --pink: #ff4db7;
    --pink-shade: #d9289a;
    --pink-ink: #a8117a;
    --red: #ff7272;
    --red-shade: #e24f52;
    --red-ink: #b8142a;
    --blue: #1b9fd7;
    --blue-shade: #0d7db4;
    --blue-ink: #2a2e88;
    --blue-ring: #2ec0ef;
  }
  html, body {
    margin: 0;
    padding: 0;
    overflow: hidden;
    background: var(--bg);
  }
  .chart {
    position: relative;
    width: 1200px;
    height: 1173px;
    background: var(--bg);
    overflow: hidden;
  }
  .chart__network {
    position: absolute;
    inset: 0;
    width: 1200px;
    height: 1173px;
  }
  .link {
    stroke: var(--line);
    stroke-width: 13;
    stroke-linecap: round;
  }
  .node__ring { fill: var(--line); }
  .team-label {
    font-family: "Arimo", Arial, sans-serif;
    font-weight: 700;
    font-size: 23px;
    text-anchor: middle;
  }
  .team-label--sales { fill: var(--yellow-ink); }
  .team-label--product { fill: var(--orange-ink); }
  .team-label--supply { fill: var(--green-ink); }
  .team-label--marketing { fill: var(--pink-ink); }
  .team-label--digital { fill: var(--red-ink); }
  .team-label--hr { fill: var(--blue-ink); }
  .chart__title {
    position: absolute;
    left: 0;
    right: 0;
    top: 1058px;
    margin: 0;
    text-align: center;
    font-family: "Arimo", Arial, sans-serif;
    font-weight: 700;
    font-size: 72px;
    line-height: 1;
    color: var(--title);
  }
</style>
</head>
<body>
<main class="chart">
  <svg class="chart__network" viewBox="0 0 1200 1173" xmlns="http://www.w3.org/2000/svg" aria-label="Network organisation of six teams">
    <defs>
      <radialGradient id="fill-sales" cx="45%" cy="35%" r="70%">
        <stop offset="0.55" stop-color="var(--yellow)"/><stop offset="1" stop-color="var(--yellow-shade)"/>
      </radialGradient>
      <radialGradient id="fill-product" cx="45%" cy="35%" r="70%">
        <stop offset="0.55" stop-color="var(--orange)"/><stop offset="1" stop-color="var(--orange-shade)"/>
      </radialGradient>
      <radialGradient id="fill-supply" cx="45%" cy="35%" r="70%">
        <stop offset="0.55" stop-color="var(--green)"/><stop offset="1" stop-color="var(--green-shade)"/>
      </radialGradient>
      <radialGradient id="fill-marketing" cx="45%" cy="35%" r="70%">
        <stop offset="0.55" stop-color="var(--pink)"/><stop offset="1" stop-color="var(--pink-shade)"/>
      </radialGradient>
      <radialGradient id="fill-digital" cx="45%" cy="35%" r="70%">
        <stop offset="0.55" stop-color="var(--red)"/><stop offset="1" stop-color="var(--red-shade)"/>
      </radialGradient>
      <radialGradient id="fill-hr" cx="45%" cy="35%" r="70%">
        <stop offset="0.55" stop-color="var(--blue)"/><stop offset="1" stop-color="var(--blue-shade)"/>
      </radialGradient>
      <linearGradient id="gloss" x1="0" y1="0" x2="0" y2="1">
        <stop offset="0" stop-color="#fff" stop-opacity="0.6"/><stop offset="1" stop-color="#fff" stop-opacity="0.05"/>
      </linearGradient>
    </defs>

    <g class="links">
      <line class="link" x1="387" y1="173" x2="809" y2="173"/>
      <line class="link" x1="809" y1="173" x2="1012" y2="537"/>
      <line class="link" x1="1012" y1="537" x2="809" y2="882"/>
      <line class="link" x1="809" y1="882" x2="387" y2="882"/>
      <line class="link" x1="387" y1="882" x2="169" y2="537"/>
      <line class="link" x1="169" y1="537" x2="387" y2="173"/>
      <line class="link" x1="387" y1="173" x2="809" y2="882"/>
      <line class="link" x1="809" y1="173" x2="387" y2="882"/>
      <line class="link" x1="169" y1="537" x2="1012" y2="537"/>
    </g>

    <g class="node node--sales">
      <circle class="node__ring" cx="387" cy="173" r="137"/>
      <circle cx="387" cy="173" r="124" fill="url(#fill-sales)"/>
      <ellipse cx="372" cy="110" rx="80" ry="42" fill="url(#gloss)"/>
      <text class="team-label team-label--sales" x="387" y="157">Team</text>
      <text class="team-label team-label--sales" x="387" y="185">Sales &amp;</text>
      <text class="team-label team-label--sales" x="387" y="213">Consulting</text>
    </g>

    <g class="node node--product">
      <circle class="node__ring" cx="809" cy="173" r="137"/>
      <circle cx="809" cy="173" r="124" fill="url(#fill-product)"/>
      <ellipse cx="794" cy="110" rx="80" ry="42" fill="url(#gloss)"/>
      <text class="team-label team-label--product" x="809" y="157">Team</text>
      <text class="team-label team-label--product" x="809" y="185">Product</text>
      <text class="team-label team-label--product" x="809" y="213">Management</text>
    </g>

    <g class="node node--supply">
      <circle cx="1012" cy="537" r="140" fill="var(--green-ring)"/>
      <circle class="node__ring" cx="1012" cy="537" r="133"/>
      <circle cx="1012" cy="537" r="122" fill="url(#fill-supply)"/>
      <ellipse cx="997" cy="474" rx="80" ry="42" fill="url(#gloss)"/>
      <text class="team-label team-label--supply" x="1012" y="528">Team</text>
      <text class="team-label team-label--supply" x="1012" y="556">Supply Chain</text>
    </g>

    <g class="node node--marketing">
      <circle class="node__ring" cx="169" cy="537" r="137"/>
      <circle cx="169" cy="537" r="124" fill="url(#fill-marketing)"/>
      <ellipse cx="154" cy="474" rx="80" ry="42" fill="url(#gloss)"/>
      <text class="team-label team-label--marketing" x="169" y="515">Team</text>
      <text class="team-label team-label--marketing" x="169" y="543">Marketing &amp;</text>
      <text class="team-label team-label--marketing" x="169" y="571">Communication</text>
    </g>

    <g class="node node--digital">
      <circle class="node__ring" cx="387" cy="882" r="137"/>
      <circle cx="387" cy="882" r="124" fill="url(#fill-digital)"/>
      <ellipse cx="372" cy="819" rx="80" ry="42" fill="url(#gloss)"/>
      <text class="team-label team-label--digital" x="387" y="864">Team</text>
      <text class="team-label team-label--digital" x="387" y="892">Smart Digital</text>
      <text class="team-label team-label--digital" x="387" y="920">Development</text>
    </g>

    <g class="node node--hr">
      <circle cx="809" cy="882" r="140" fill="var(--blue-ring)"/>
      <circle class="node__ring" cx="809" cy="882" r="133"/>
      <circle cx="809" cy="882" r="122" fill="url(#fill-hr)"/>
      <ellipse cx="794" cy="819" rx="80" ry="42" fill="url(#gloss)"/>
      <text class="team-label team-label--hr" x="809" y="864">Team</text>
      <text class="team-label team-label--hr" x="809" y="892">Human</text>
      <text class="team-label team-label--hr" x="809" y="920">Resources</text>
    </g>
  </svg>

  <h1 class="chart__title">vireLattice</h1>
</main>
</body>
</html>
```